Sleep Consulting Business

Hello I need a business card design with similar colors to my logo that was created. I help mom/parents whose little ones are having sleep issues. Are you able to recreate the picture with the girl sleeping onto a business card using a picture that I provide. That would be one side with my logo on top and on the other side would the following:
My name (in bigger letters than the rest. maybe written in script
title
email
website
phone
instagram
I have included color Inspo
Full Name, number, email, website, ig page

```html
<!DOCTYPE html>
<html lang="en">
<head>
<meta charset="UTF-8">
<title>Pinecrest Sleep Co. – Business Card</title>
<link href="https://fonts.googleapis.com/css2?family=Montserrat:wght@400;500;700&display=swap" rel="stylesheet">
<style>
  :root {
    --page: #ececea;
    --taupe: #a0928b;
    --coral: #e0907a;
    --brown: #8f7d76;
    --white: #ffffff;
  }
  html, body {
    margin: 0;
    width: 1200px;
    height: 1200px;
    overflow: hidden;
    background: var(--page);
    font-family: "Montserrat", sans-serif;
  }
  .sheet {
    position: relative;
    width: 1200px;
    height: 1200px;
  }
  .card {
    position: absolute;
    left: 250px;
    width: 700px;
    height: 400px;
    border-radius: 34px;
    overflow: hidden;
    background: var(--taupe);
    box-shadow: 0 6px 18px rgba(0,0,0,0.12);
  }
  .card--front { top: 150px; }
  .card--back  { top: 650px; }
  .card__bg {
    position: absolute;
    inset: 0;
    width: 100%;
    height: 100%;
  }
  .brand {
    position: absolute;
    display: flex;
    align-items: center;
    gap: 14px;
    font-weight: 500;
    letter-spacing: 0.04em;
    white-space: nowrap;
    transform: translate(-50%, -50%);
  }
  .brand__dot {
    border-radius: 50%;
    flex: none;
  }
  .card--front .brand {
    left: 300px;
    top: 125px;
    font-size: 32px;
    color: var(--brown);
  }
  .card--front .brand__dot {
    width: 28px; height: 28px;
    background: var(--brown);
  }
  .card--back .brand {
    left: 50%;
    top: 50%;
    font-size: 50px;
    color: var(--white);
  }
  .card--back .brand__dot {
    width: 42px; height: 42px;
    background: var(--white);
  }
  .person {
    position: absolute;
    left: 58px;
    top: 300px;
    color: var(--white);
  }
  .person__name {
    font-weight: 700;
    font-size: 30px;
    letter-spacing: 0.01em;
    line-height: 1.05;
  }
  .person__title {
    font-size: 18px;
    font-weight: 400;
    letter-spacing: 0.02em;
    margin-top: 2px;
  }
  .divider {
    position: absolute;
    left: 390px;
    top: 282px;
    width: 1px;
    height: 96px;
    background: rgba(255,255,255,0.55);
  }
  .contact {
    position: absolute;
    left: 430px;
    top: 268px;
    margin: 0;
    padding: 0;
    list-style: none;
    color: var(--white);
    font-size: 17px;
    line-height: 27px;
  }
  .contact__item {
    display: flex;
    align-items: center;
    gap: 9px;
  }
  .contact__icon {
    width: 17px;
    height: 17px;
    flex: none;
  }
</style>
</head>
<body>
<main class="sheet">

  <section class="card card--front" aria-label="Business card front">
    <svg class="card__bg" viewBox="0 0 700 400" preserveAspectRatio="none" aria-hidden="true">
      <path d="M0 0 H700 V72 C610 212 390 270 0 266 Z" fill="var(--white)"/>
      <path d="M0 0 H700 V64 C606 204 390 264 0 262 Z" fill="var(--coral)"/>
      <path d="M0 0 H700 V52 C600 194 390 256 0 258 Z" fill="var(--white)"/>
    </svg>

    <div class="brand">
      <span class="brand__dot"></span>
      <span class="brand__name">Pinecrest Sleep Co.</span>
    </div>

    <div class="person">
      <div class="person__name">FULL NAME</div>
      <div class="person__title">POSITION</div>
    </div>

    <div class="divider"></div>

    <ul class="contact">
      <li class="contact__item">
        <svg class="contact__icon" viewBox="0 0 16 16" aria-hidden="true"><path d="M3.5 1.5 L6 4 L4.6 5.8 C5.5 7.8 8.2 10.5 10.2 11.4 L12 10 L14.5 12.5 L12.6 14.4 C7.5 14 2 8.5 1.6 3.4 Z" fill="var(--white)"/></svg>
        <span>(000) 000 0000</span>
      </li>
      <li class="contact__item">
        <svg class="contact__icon" viewBox="0 0 16 16" aria-hidden="true"><rect x="1.5" y="3.5" width="13" height="9" fill="none" stroke="var(--white)" stroke-width="1.4"/><path d="M1.5 3.5 L8 9 L14.5 3.5" fill="none" stroke="var(--white)" stroke-width="1.4"/></svg>
        <span>email@company.com</span>
      </li>
      <li class="contact__item">
        <svg class="contact__icon" viewBox="0 0 16 16" aria-hidden="true"><circle cx="8" cy="8" r="6.5" fill="none" stroke="var(--white)" stroke-width="1.2"/><ellipse cx="8" cy="8" rx="2.8" ry="6.5" fill="none" stroke="var(--white)" stroke-width="1.1"/><path d="M1.5 8 H14.5 M2.5 5 H13.5 M2.5 11 H13.5" stroke="var(--white)" stroke-width="1.1"/></svg>
        <span>www.company.com</span>
      </li>
      <li class="contact__item">
        <svg class="contact__icon" viewBox="0 0 16 16" aria-hidden="true"><rect x="2" y="2" width="12" height="12" rx="2" fill="none" stroke="var(--white)" stroke-width="1.4"/></svg>
        <span>/pinecrestsleep</span>
      </li>
    </ul>
  </section>

  <section class="card card--back" aria-label="Business card back">
    <div class="brand">
      <span class="brand__dot"></span>
      <span class="brand__name">Pinecrest Sleep Co.</span>
    </div>
  </section>

</main>
</body>
</html>
```